Oven Cleaning Business owner needs business card design

Hi there,
Would like for a business card to be designed for myself, the owner of a professional oven cleaning business on the Sunshine Coast.
Would like it to look sleek, and modern-ish. Bit creative is encouraged too.
Include following:
Name/title: Corin ter Haghe, Owner
Phone number: 1300 482 916
Email: info@hearthshinecrew.com.au
Website: www.hearthshinecrew.com.au

```html
<!DOCTYPE html>
<html lang="en">
<head>
<meta charset="utf-8">
<title>Hearthshine Crew – Business Card</title>
<link rel="stylesheet" href="https://fonts.googleapis.com/css2?family=Montserrat:wght@400;500;700&display=swap">
<style>
  :root {
    --teal: #12dbd6;
    --teal-deep: #1ec9cc;
    --ink: #000000;
    --paper: #fdfcf8;
    --white: #ffffff;
  }
  * { margin: 0; padding: 0; box-sizing: border-box; }
  html, body { width: 1200px; height: 857px; overflow: hidden; }
  body {
    position: relative;
    background: var(--teal);
    font-family: "Montserrat", sans-serif;
  }
  .backdrop-shape { position: absolute; left: 0; top: 0; }

  .card {
    position: absolute;
    width: 600px;
    height: 342px;
    border-radius: 14px;
    background: var(--paper);
    overflow: hidden;
  }
  .card--front { left: 285px; top: 55px; }
  .card--back  { left: 290px; top: 427px; }

  /* Front decorations */
  .front-accent-dot {
    position: absolute;
    left: 74px; top: 313px;
    width: 96px; height: 96px;
    border-radius: 50%;
    background: var(--teal-deep);
  }
  .front-band {
    position: absolute;
    left: 117px; top: 300px;
    width: 500px; height: 60px;
    background: var(--ink);
    border-top-left-radius: 46px;
  }

  /* Brand lockup */
  .brand {
    position: absolute;
    display: flex;
    flex-direction: column;
    align-items: center;
    transform: translateX(-50%);
  }
  .brand__dot {
    border-radius: 50%;
    background: var(--teal-deep);
  }
  .brand__name {
    font-weight: 700;
    color: var(--ink);
    text-transform: uppercase;
    text-align: center;
    letter-spacing: 0.04em;
    line-height: 1.05;
  }
  .card--front .brand { left: 300px; top: 88px; }
  .card--front .brand__dot { width: 70px; height: 70px; margin-bottom: 22px; }
  .card--front .brand__name { font-size: 28px; }

  .card--back .brand { left: 142px; top: 112px; }
  .card--back .brand__dot { width: 52px; height: 52px; margin-bottom: 16px; }
  .card--back .brand__name { font-size: 21px; }

  /* Back layout */
  .back-notch {
    position: absolute;
    left: 0; top: 82px;
    width: 18px; height: 157px;
    background: var(--ink);
    border-radius: 0 18px 18px 0;
  }
  .back-panel {
    position: absolute;
    left: 284px; top: 0;
    width: 316px; height: 342px;
    background: var(--ink);
    border-bottom-left-radius: 44px;
  }
  .person { position: absolute; left: 34px; top: 100px; }
  .person__name {
    font-weight: 700;
    font-size: 20px;
    color: var(--white);
    letter-spacing: -0.01em;
  }
  .person__title {
    margin-top: 8px;
    margin-left: 4px;
    font-weight: 400;
    font-size: 12px;
    letter-spacing: 15px;
    color: var(--teal);
  }
  .contact {
    position: absolute;
    left: 28px; top: 191px;
    list-style: none;
  }
  .contact__item {
    display: flex;
    align-items: center;
    gap: 9px;
    height: 22px;
    font-size: 14.5px;
    font-weight: 400;
    color: var(--white);
  }
  .contact__icon { width: 16px; height: 16px; flex: none; }
</style>
</head>
<body>

<svg class="backdrop-shape" width="1200" height="857" viewBox="0 0 1200 857" aria-hidden="true">
  <path d="M451 0 L567 0 L567 857 L491 857 C200 857 0 700 0 430 C0 180 200 0 451 0 Z" fill="var(--ink)"/>
</svg>

<section class="card card--front" aria-label="Card front">
  <div class="front-accent-dot"></div>
  <div class="front-band"></div>
  <div class="brand">
    <span class="brand__dot"></span>
    <span class="brand__name">Hearthshine Crew</span>
  </div>
</section>

<section class="card card--back" aria-label="Card back">
  <div class="back-notch"></div>
  <div class="brand">
    <span class="brand__dot"></span>
    <span class="brand__name">Hearthshine Crew</span>
  </div>
  <div class="back-panel">
    <div class="person">
      <p class="person__name">CORIN TER HAGHE</p>
      <p class="person__title">OWNER</p>
    </div>
    <ul class="contact">
      <li class="contact__item">
        <svg class="contact__icon" viewBox="0 0 16 16" aria-hidden="true">
          <circle cx="8" cy="8" r="7" fill="none" stroke="var(--teal)" stroke-width="1.3"/>
          <path d="M6 4.5 L7 6.6 L6.2 7.4 C6.7 8.5 7.5 9.3 8.6 9.8 L9.4 9 L11.5 10 L11 11.4 C8 11.4 4.6 8 4.6 5 Z" fill="var(--teal)"/>
        </svg>
        1300 482 916
      </li>
      <li class="contact__item">
        <svg class="contact__icon" viewBox="0 0 16 16" aria-hidden="true">
          <circle cx="8" cy="8" r="7" fill="none" stroke="var(--teal)" stroke-width="1.3"/>
          <circle cx="8" cy="8" r="3.6" fill="none" stroke="var(--white)" stroke-width="1"/>
          <path d="M4.4 8 H11.6 M8 4.4 C6.6 6 6.6 10 8 11.6 C9.4 10 9.4 6 8 4.4" fill="none" stroke="var(--white)" stroke-width="0.8"/>
        </svg>
        www.hearthshinecrew.com.au
      </li>
      <li class="contact__item">
        <svg class="contact__icon" viewBox="0 0 16 16" aria-hidden="true">
          <circle cx="8" cy="8" r="7" fill="none" stroke="var(--teal)" stroke-width="1.3"/>
          <text x="8" y="11" text-anchor="middle" font-family="Montserrat, sans-serif" font-size="8.5" fill="var(--white)">@</text>
        </svg>
        info@hearthshinecrew.com.au
      </li>
    </ul>
  </div>
</section>

</body>
</html>
```